lawn sign

Lawn Sign
Roofing Gutters Windows

Target Market(s)

roofing

Font styles to use
Sans Serif

Colors
86cfc6
33a6d7
fbee3f
faa54b

Requirements
Must have
• my logo
Nice to have
• designer for now

```html
<!DOCTYPE html>
<html lang="en">
<head>
<meta charset="utf-8">
<title>Lawn Sign – Roofing Gutters Windows</title>
<link rel="stylesheet" href="https://fonts.googleapis.com/css2?family=Cinzel:wght@400;600&family=Oswald:wght@500;700&display=swap">
<style>
  :root {
    --backdrop: #808080;
    --sign-green: #9ad14f;
    --sign-blue: #1f7ab8;
    --sign-white: #ffffff;
    --navy: #16264a;
    --brand-green: #3f9a2e;
    --mark-tint: #c9e6a6;
  }
  html, body {
    margin: 0;
    padding: 0;
    width: 1200px;
    height: 1200px;
    overflow: hidden;
    background: var(--backdrop);
  }
  .canvas {
    width: 1200px;
    height: 1200px;
    display: flex;
    align-items: center;
    justify-content: center;
  }
  .lawn-sign {
    width: 895px;
    height: 1157px;
    display: block;
  }
  .headline { font-family: "Cinzel", serif; font-weight: 600; fill: var(--navy); }
  .services { font-family: "Oswald", sans-serif; font-weight: 700; fill: var(--sign-white); }
  .brand-name { font-family: "Cinzel", serif; font-weight: 400; fill: var(--brand-green); }
  .call-label { font-family: "Oswald", sans-serif; font-weight: 700; fill: var(--navy); }
  .call-number { font-family: "Oswald", sans-serif; font-weight: 500; fill: var(--sign-white); }
  .website { font-family: "Cinzel", serif; font-weight: 400; fill: var(--sign-white); }
</style>
</head>
<body>
<main class="canvas">
  <svg class="lawn-sign" viewBox="0 0 778 1006" xmlns="http://www.w3.org/2000/svg" aria-label="Lawn sign: Roofing, Gutters, Windows">
    <rect class="panel-top" x="0" y="0" width="778" height="1006" fill="var(--sign-green)"/>
    <path class="panel-middle" d="M0 389 Q389 217 778 389 L778 670 Q389 846 0 670 Z" fill="var(--sign-white)"/>
    <path class="panel-bottom" d="M0 670 Q389 846 778 670 L778 1006 L0 1006 Z" fill="var(--sign-blue)"/>

    <text class="headline" x="50" y="163" font-size="128" textLength="678" lengthAdjust="spacingAndGlyphs">ROOFING</text>
    <text class="services" x="55" y="263" font-size="88" textLength="663" lengthAdjust="spacingAndGlyphs">GUTTERS WINDOWS</text>

    <g class="brand">
      <circle class="brand-dot" cx="253" cy="498" r="100" fill="var(--mark-tint)"/>
      <text class="brand-name" text-anchor="end" x="643" y="588" font-size="46">HARTWELL</text>
      <text class="brand-name" text-anchor="end" x="643" y="633" font-size="30">RESTORATION</text>
      <text class="brand-name" text-anchor="end" x="643" y="671" font-size="30" textLength="436" lengthAdjust="spacingAndGlyphs">REMODELING GROUP LLC</text>
    </g>

    <text x="83" y="881" font-size="86" textLength="612" lengthAdjust="spacingAndGlyphs"><tspan class="call-label">CALL:</tspan><tspan class="call-number"> (555) 014-2270</tspan></text>
    <text class="website" x="173" y="948" font-size="34" textLength="432" lengthAdjust="spacingAndGlyphs">WWW.HARTWELLLLC.COM</text>
  </svg>
</main>
</body>
</html>
```